Industrial Professional Business Card Design (Vantrel Systems)

Would like professional looking business cards. Not too busy leaning towards minimal. Should have a slogan like:
"Industrial Automation and Control".

We are a tech company that programs industrial PLC computers. We also develop custom hardware solutions. Please use the logo for inspiration.

Target Market(s)

Mining, industrial, processing, automation, factory

Industry/Entity Type

Engineering

Contact Information for Business Card

Name, phone, email, website. job title.

Font styles to use
Other font styles liked:
• droid sans

Requirements
Must have
• Use colours that go well with the logo. Not too busy design.

```html
<!DOCTYPE html>
<html lang="en">
<head>
<meta charset="utf-8">
<title>Vantrel Systems — Business Card</title>
<link href="https://fonts.googleapis.com/css2?family=Open+Sans:wght@400;700&display=swap" rel="stylesheet">
<style>
  :root {
    --navy: #1d4b7b;
    --orange: #f26522;
    --text-grey: #4a4f57;
    --card: #ffffff;
    --backdrop: #d4d4d1;
  }
  * { margin: 0; padding: 0; box-sizing: border-box; }
  html, body { width: 1200px; height: 801px; overflow: hidden; }
  body {
    background: var(--backdrop);
    font-family: "Open Sans", sans-serif;
    display: flex;
    align-items: center;
    justify-content: center;
    gap: 36px;
  }
  .card {
    width: 546px;
    height: 312px;
    background: var(--card);
    border-bottom: 3px solid var(--orange);
    position: relative;
    box-shadow: 0 6px 18px rgba(0,0,0,0.12);
  }
  .wordmark {
    display: flex;
    align-items: center;
    gap: 10px;
    color: var(--navy);
    font-weight: 400;
    white-space: nowrap;
  }
  .wordmark-dot {
    display: inline-block;
    border-radius: 50%;
    background: var(--orange);
    flex: none;
  }
  /* info side */
  .card-info { display: flex; align-items: center; }
  .card-info .brand {
    width: 50%;
    display: flex;
    justify-content: center;
  }
  .card-info .wordmark { font-size: 22px; }
  .card-info .wordmark-dot { width: 16px; height: 16px; }
  .divider {
    width: 1.5px;
    height: 150px;
    background: var(--orange);
  }
  .details { padding-left: 28px; color: var(--text-grey); font-size: 11.5px; line-height: 1.5; }
  .person-name { color: var(--navy); font-weight: 700; font-size: 16px; letter-spacing: 0.5px; line-height: 1.2; }
  .person-title { margin-bottom: 10px; }
  .address { margin-bottom: 10px; }
  .contact-list { list-style: none; }
  .contact-list li { display: flex; align-items: center; gap: 7px; }
  .contact-list svg { width: 11px; height: 11px; fill: var(--navy); flex: none; }
  /* brand side */
  .card-brand { display: flex; align-items: center; justify-content: center; }
  .card-brand .wordmark { font-size: 38px; gap: 14px; }
  .card-brand .wordmark-dot { width: 26px; height: 26px; }
</style>
</head>
<body>
  <section class="card card-info">
    <div class="brand">
      <div class="wordmark"><span class="wordmark-dot"></span>Vantrel Systems</div>
    </div>
    <div class="divider"></div>
    <div class="details">
      <p class="person-name">DARIEN KOLBY</p>
      <p class="person-title">Owner/CEO</p>
      <p class="address">210 - 4471 Halden Rd<br>Marlow, BC V9K2T4</p>
      <ul class="contact-list">
        <li><svg viewBox="0 0 24 24" aria-hidden="true"><path d="M6.6 10.8a15 15 0 0 0 6.6 6.6l2.2-2.2a1 1 0 0 1 1-.25 11.4 11.4 0 0 0 3.6.57 1 1 0 0 1 1 1V20a1 1 0 0 1-1 1A17 17 0 0 1 3 4a1 1 0 0 1 1-1h3.5a1 1 0 0 1 1 1c0 1.25.2 2.45.57 3.57a1 1 0 0 1-.25 1z"/></svg>(555) 318-2746</li>
        <li><svg viewBox="0 0 24 24" aria-hidden="true"><path d="M3 9c0-3 4-5 9-5s9 2 9 5v2h-5V9H8v2H3zM6 12h12l2 8H4z"/></svg>(555) 402-6190 ext 114</li>
        <li><svg viewBox="0 0 24 24" aria-hidden="true"><path d="M2 5h20v14H2zm2 2v.5l8 5 8-5V7z"/></svg>darien@vantrelsystems.com</li>
        <li><svg viewBox="0 0 24 24" aria-hidden="true"><path d="M12 2a10 10 0 1 0 0 20 10 10 0 0 0 0-20zm0 2a8 8 0 0 1 7.7 6H16l-2-3-3 1-1 3 3 2v4l-2 2A8 8 0 0 1 12 4z"/></svg>www.vantrelsystems.com</li>
      </ul>
    </div>
  </section>

  <section class="card card-brand">
    <div class="wordmark"><span class="wordmark-dot"></span>Vantrel Systems</div>
  </section>
</body>
</html>
```